For Creative Minds: A Simple Clean Book Cover that Stands Out

This will be a christian book teaching christians about divine healing. It is part of a series called "Morning Step Collection". I want the book cover to communicate the idea of healing, and specifically heavenly healing from God. These are some of the specifications below

1. General
Book to be published on print harbor platform
Dimensions: 6 x 9 inches, Paperback
Number of words: Estimated to be about 60,000 words.
Please use Indesign for design and submit the final Indesign source files along with the final design.

2. Cover image.
Image can be either human or any object that can communicate the idea above. No human faces to show up prominently.
High quality image is highly solicited.

3. Title:
" Forty Evenings Toward Lasting Renewal Within Your Soul"

3. Author name
Preferably should appear below. Open to creative ideas with titles that are better placed above.

Author's Name: Duncan Ferrow

3. Layout
Should not be too busy.
Simple and clean layout appeals more to me.

4. Series name
AS noted above, this book will be part of a series called " Morning Step Collection". I want this series name to appear somewhere in the cover and to have a simple but unique design that will be used for all subsequent titles. The Title of the book should have the emphasis.

I have attached a sample cover for one of my monthly devotional books which I choose from a contest.

ABOUT THE AUTHOR
Duncan Ferrow represents the blessed combination of Physician and Minister, bringing healing not only to the physical body but to the spiritual heart. He currently works as the Director of the Hospital Medicine Program at the Bellhaven County Care Campus in Iowa, USA. He is the Founder of Lantern & Vine Fellowship, a teaching ministry that seeks to bring believers into the fullness of grace — the glory of God — through conferences, seminars and books.

One of his notable quotes is “The Word of God is the most potent and efficient remedy for all the ailments of humanity.” This clearly portrays his experience with the Word as a Physician who is familiar with the powers, both natural and supernatural, to mend broken human beings. 

He currently lives in Iowa, USA with his wife, Lu Tessin, and daughter, Rosalind. You can reach out to Patrick using the contact information listed below.

BLURB
As a Physician and Minister, I have seen the power of modern medicine to bring about healing in the body and mind as well as the operation of the power of God to produce amazing medical results. However, many people are just not aware of the reality of divine healing. To some, it is a myth, belief or some "faith talk" in the heart. Medical miracles are real and we should take full advantage of it. As much as a love being a physician and treat patients in the hospital, I have come to see both its amazing successes and many limitations.

Industry/Entity Type

Christian

Font styles to use
Serif

Colors

Designer to choose colors to be used in the design.

Requirements
Should not have
• Too stylistic fonts

```html
<!DOCTYPE html>
<html lang="en">
<head>
<meta charset="utf-8">
<title>Forty Evenings Toward Lasting Renewal Within Your Soul — Duncan Ferrow</title>
<link rel="stylesheet" href="https://fonts.googleapis.com/css2?family=Cinzel:wght@400&family=Allura&display=swap">
<style>
  :root {
    --backdrop: #131315;
    --sky-top: #4a3120;
    --sky-mid: #4f3a25;
    --sky-haze: #6e7a62;
    --glow: #f3e6b8;
    --ground: #362516;
    --type-light: #f1efe9;
  }
  html, body {
    margin: 0;
    width: 1200px;
    height: 1200px;
    overflow: hidden;
    background: var(--backdrop);
  }
  .book-cover {
    position: absolute;
    left: 236px;
    top: 75px;
    width: 728px;
    height: 1050px;
    overflow: hidden;
    color: var(--type-light);
  }
  .cover-photo {
    position: absolute;
    inset: 0;
    background:
      radial-gradient(ellipse 240px 150px at 360px 890px, var(--glow) 0%, rgba(230,205,140,0.7) 30%, rgba(180,160,100,0.25) 65%, rgba(0,0,0,0) 100%),
      radial-gradient(ellipse 520px 200px at 420px 820px, rgba(140,160,130,0.55) 0%, rgba(0,0,0,0) 100%),
      linear-gradient(180deg, var(--sky-top) 0%, var(--sky-mid) 55%, var(--sky-haze) 78%, #8a7a52 88%, var(--ground) 92%, var(--ground) 100%);
  }
  .series-name {
    position: absolute;
    top: 6px;
    left: 0;
    right: 0;
    text-align: center;
    font-family: "Cinzel", serif;
    font-size: 20px;
    letter-spacing: 0.32em;
    text-transform: uppercase;
  }
  .book-title {
    position: absolute;
    top: 62px;
    left: 0;
    right: 0;
    margin: 0;
    text-align: center;
    font-family: "Allura", cursive;
    font-weight: 400;
    line-height: 1;
  }
  .title-lead { display: block; font-size: 96px; }
  .title-joiner { display: block; font-size: 40px; margin-top: -4px; }
  .title-tail { display: block; font-size: 56px; margin-top: 2px; }
  .author-name {
    position: absolute;
    bottom: 14px;
    left: 0;
    right: 0;
    text-align: center;
    font-family: "Cinzel", serif;
    font-size: 28px;
    letter-spacing: 0.2em;
    text-transform: uppercase;
  }
</style>
</head>
<body>
  <main class="book-cover">
    <div class="cover-photo" role="img" aria-label="Photograph of a tall wooden cross silhouetted against a hazy sunset sky, with a person standing beside it with arms raised toward the light"></div>
    <div class="series-name">Morning Step Collection</div>
    <h1 class="book-title">
      <span class="title-lead">Forty Evenings</span>
      <span class="title-joiner">Toward</span>
      <span class="title-tail">Lasting Renewal Within Your Soul</span>
    </h1>
    <div class="author-name">Duncan Ferrow</div>
  </main>
</body>
</html>
```